Website redesign for a Cloud Advisory business

We are looking to revisit our existing brand and website, with a view to updating both. Looking for concepts and designs for how the website might look, flow and feel. Current website is: www.brightlane.com.au

Scope and Deliverables: Concept design for the home page and one internal page.

We do not expect you to design all the pages and all the elements of the website at this stage.

This job is not for the full website design, but just for concepts that we can start with when we go into the full website design.

We would love to see a design feature based on our name, logo, or industry, which can run through banners and other collateral (chirpnet banner, ads on Findora, corporate documents etc).

We want the brand to properly depict what we bring/deliver to businesses when consulting to them and this should extend to the colour scheme, logo, font (perhaps updated) and copy (which will be supplied).

Our brand should suitably communicate our ability, knowledge and extensive experience within the Cloud space.

It should express and evoke credibility, knowledge and understanding of the Cloud space, independence, gravitas, reliability, efficiency, trust, expertise, approachability, service delivery but be uncomplicated, practical and use plain speaking language.

Colours that reinforce this might include: Blues, blacks, silver, white, grey and our existing orange.

Website designs that we like or have referenced include:

Skyvault: http://skyvault.com.au/ - This has good information but looks a little amateur in it’s cartoon like design and colour scheme. Also, this seems to be aimed at clients more interested in price than design and what we are going for is a little more high end.

Nimbuspath: https://www.nimbuspath.com.au/ - This site has merit in its’ setup but little call to action on the home page, especially before the scroll line. I like the set up of the Case Studies page however I’d look to make it more prominent by having it set up 3 across rather than the 4 they have. Something such as this: https://www.tallyrig.com/case-studies

Pelwyn: http://www.pelwyn.com.au/#home4 - This page is a good one as far as selling services and information on the company. I quite like it.

BorealIT: http://www.borealit.com.au/ - While I don’t think is particularly creative, it does practically depict the services we offer in a fairly clear way and might be a bit of a basic (albeit dull) template to follow.

QRV: https://store.qrv.com/us/Product-Family/QRV-Advisory-Services/QRV-Cloud-Advisory-Service/p/QRV-Services-Cloud-Advisory - This offers substantial information but is probably a little confusing although the roll-over drop down menus have merit.

LUP: http://www.lup.net.au/en/services/ - While this in not quite what we are looking for, the colour scheme gives it more gravitas and quality.

As another reference, this website and the way they present their case studies is also something we like, although I’d like them shown 3 up, side by side…. https://www.tallyrig.com/case-studies.

We have added a page layout and page purpose document.

Target Market(s)

Corporates, small - medium business, direct referrals, via search results

Industry/Entity Type

Business

Number of Pages Required

1 page

Font styles to use
Sans Serif

Colors
85abd2
0455a3
000000
f37122
5c5c5c

Requirements
Must have
• Website must be mobile device compatible.
• Concept design for the home page.
Nice to have
• We would love to see a design feature based on our name, logo, or industry, which can run through banners and other collateral (chirpnet banner, ads on Findora, corporate documents etc).

```html
<!DOCTYPE html>
<html lang="en">
<head>
<meta charset="utf-8">
<title>Brightlane – Impartial Cloud Solutions</title>
<link rel="stylesheet" href="https://fonts.googleapis.com/css2?family=Ubuntu:wght@400;500;700&family=Arimo:wght@400;700&display=swap">
<style>
:root{
  --orange:#f15a22;
  --orange-soft:#f37122;
  --ink:#333333;
  --grey-text:#5c5c5c;
  --grey-band:#e6e6e6;
  --card-grey:#efefef;
  --dark-btn:#3d3d3d;
  --dark-band:#262626;
  --white:#ffffff;
  --red:#d71a21;
  --black:#111111;
}
*{box-sizing:border-box;margin:0;padding:0}
html,body{width:1200px;height:2400px;overflow:hidden;background:var(--white)}
body{position:relative;font-family:"Arimo",Arial,sans-serif;color:var(--ink)}
.abs{position:absolute}

/* header */
.site-header{left:0;top:0;width:1200px;height:125px;background:var(--white)}
.brand{left:48px;top:32px;display:flex;align-items:center;gap:12px}
.brand-mark{width:40px;height:40px;background:var(--orange)}
.brand-name{font-family:"Ubuntu",sans-serif;font-weight:700;font-size:38px;color:var(--black);letter-spacing:1px}
.brand-tag{left:100px;top:82px;font-size:12px;color:var(--black);letter-spacing:.5px}
.contact-list{left:928px;top:26px;list-style:none;font-size:14px;color:var(--grey-text)}
.contact-list li{display:flex;align-items:center;gap:8px;height:23px}
.contact-list svg{width:14px;height:14px;fill:var(--orange)}

/* nav */
.main-nav{left:0;top:125px;width:1200px;height:45px;background:var(--orange);display:flex;align-items:center;padding-left:65px}
.main-nav a{color:var(--white);text-decoration:none;font-size:14px;margin-right:40px}

/* hero */
.hero{left:0;top:170px;width:1200px;height:537px;background:linear-gradient(90deg,#ffffff 0%,#f1f1f1 55%,#e3e3e3 100%)}
.hero-photo{left:600px;top:0;width:600px;height:537px;background:radial-gradient(ellipse at 58% 60%,#3b6ea8 0%,#2f5a8c 30%,rgba(220,220,220,0) 62%)}
.hero-welcome{left:46px;top:172px;font-family:"Ubuntu",sans-serif;font-size:42px;color:var(--ink)}
.hero-title{left:46px;top:224px;font-family:"Ubuntu",sans-serif;font-weight:700;font-size:39px;color:var(--orange);letter-spacing:.5px}
.hero-sub{left:50px;top:276px;font-size:18px;color:var(--ink)}
.btn-primary{left:48px;top:326px;width:213px;height:48px;background:var(--orange);color:var(--white);border-radius:4px;font-size:16px;display:flex;align-items:center;justify-content:center}

/* who */
.who{left:0;top:707px;width:1200px;height:352px;background:var(--grey-band)}
.section-title{width:1200px;left:0;text-align:center;font-family:"Ubuntu",sans-serif;font-weight:500;font-size:46px;color:var(--ink)}
.who .section-title{top:34px}
.divider-dots{left:364px;top:100px}
.who-text{left:84px;top:136px;width:1032px;text-align:center;font-size:16px;line-height:23px;color:var(--grey-text)}
.who-text p+p{margin-top:23px}

/* services */
.services{left:0;top:1059px;width:1200px;height:605px;background:var(--white)}
.services .section-title{top:38px}
.title-rule{left:498px;top:100px;width:208px;height:3px;background:var(--red)}
.service-card{top:147px;width:215px;height:394px;background:var(--card-grey);text-align:center}
.service-card.is-active{background:var(--orange)}
.service-icon{position:absolute;left:50px;top:20px;width:114px;height:114px;border-radius:50%;border:3px solid var(--orange);background:var(--white);display:flex;align-items:center;justify-content:center}
.is-active .service-icon{background:#4a4a4a;border-color:var(--white)}
.service-icon svg{width:44px;height:44px}
.service-name{position:absolute;left:0;width:100%;top:155px;font-family:"Ubuntu",sans-serif;font-weight:500;font-size:18px;line-height:18px;color:var(--black)}
.is-active .service-name{color:var(--white)}
.service-desc{position:absolute;left:20px;width:175px;top:207px;font-size:13px;line-height:19px;color:var(--ink)}
.is-active .service-desc{color:var(--white)}
.btn-order{position:absolute;left:37px;top:330px;width:130px;height:40px;background:var(--dark-btn);color:var(--white);font-size:15px;display:flex;align-items:center;justify-content:center}
.is-active .btn-order{background:var(--white);color:var(--ink)}

/* experts */
.experts{left:0;top:1664px;width:1200px;height:422px;background:linear-gradient(90deg,#1e1e1e 0%,#2a2a2a 45%,#3a3a3a 70%,#222 100%)}
.experts-photo{left:600px;top:0;width:400px;height:422px;background:radial-gradient(ellipse at 55% 70%,rgba(90,90,90,.55) 0%,rgba(40,40,40,0) 65%)}
.experts-title{left:0;width:1200px;top:42px;text-align:center;font-family:"Ubuntu",sans-serif;font-weight:400;font-size:34px;color:var(--white)}
.quote{left:130px;width:940px;top:108px;text-align:center;font-family:"Ubuntu",sans-serif;font-size:15.5px;line-height:26px;color:var(--white)}
.quote-author{left:0;width:1200px;top:242px;text-align:center;font-size:15px;color:var(--red)}
.slider-dots{left:542px;top:290px;display:flex;gap:8px}
.slider-dots span{width:32px;height:6px;background:#cfcfcf}
.slider-dots span:first-child{background:var(--red)}
.btn-outline{left:518px;top:326px;width:152px;height:43px;border:2px solid var(--white);color:var(--white);font-size:13px;display:flex;align-items:center;justify-content:center}

/* footer */
.site-footer{left:0;top:2086px;width:1200px;height:279px;background:var(--orange);color:var(--white)}
.footer-heading{top:26px;font-family:"Ubuntu",sans-serif;font-weight:400;font-size:23px;color:var(--white)}
.map{left:64px;top:69px;width:248px;height:114px;background:linear-gradient(135deg,#e8e6df,#d9d6cc)}
.footer-list{list-style:none;font-size:13px;line-height:23px}
.footer-list li::before{content:"•";color:#fbd2b8;margin-right:8px}
.social{left:934px;top:80px;width:240px;display:flex;flex-wrap:wrap;gap:14px 10px}
.social span{width:36px;height:36px;border-radius:50%}
.btn-subscribe{left:932px;top:214px;width:112px;height:37px;background:var(--red);color:var(--white);font-weight:700;font-size:14px;display:flex;align-items:center;justify-content:center}
.copyright-bar{left:0;top:2365px;width:1200px;height:35px;background:var(--black);color:var(--white);font-size:13px;display:flex;align-items:center;padding-left:64px}
.cards{right:60px;top:2374px;display:flex;gap:16px;font-size:11px;font-weight:700;color:#9fb6d8}
</style>
</head>
<body>

<header class="abs site-header">
  <div class="abs brand"><span class="brand-mark"></span><span class="brand-name">BRIGHTLANE</span></div>
  <div class="abs brand-tag">SYSTEMS SELECTION &amp; IMPLEMENTATION</div>
  <ul class="abs contact-list">
    <li><svg viewBox="0 0 24 24"><path d="M12 2a7 7 0 0 0-7 7c0 5 7 13 7 13s7-8 7-13a7 7 0 0 0-7-7zm0 9.5A2.5 2.5 0 1 1 12 6.5a2.5 2.5 0 0 1 0 5z"/></svg>Address: Kestrel Bay, Victoria</li>
    <li><svg viewBox="0 0 24 24"><path d="M2 5h20v14H2z M2 5l10 8 10-8" stroke="#fff" stroke-width="1.5"/></svg>Email: info@brightlane.com.au</li>
    <li><svg viewBox="0 0 24 24"><rect x="6" y="2" width="12" height="20" rx="2"/></svg>Phone: 1300 555 014</li>
  </ul>
</header>

<nav class="abs main-nav">
  <a>Home</a><a>About Us</a><a>Industry Specialties</a><a>Solutions</a><a>The Company We Keep</a><a>Case Studies &amp; Testimonials</a><a>FAQ's</a><a>Blog</a><a>Contact Us</a>
</nav>

<section class="abs hero">
  <div class="abs hero-photo" role="img" aria-label="Photo of a smiling consultant in a blue shirt in a bright office"></div>
  <div class="abs hero-welcome">Welcome</div>
  <h1 class="abs hero-title">IMPARTIAL CLOUD SOLUTIONS</h1>
  <p class="abs hero-sub">We provide impartial advice on cloud solutions ensuring it's always right for you.</p>
  <div class="abs btn-primary">Book a Free Consultation</div>
</section>

<section class="abs who">
  <h2 class="abs section-title">Who Are We?</h2>
  <svg class="abs divider-dots" width="472" height="12" viewBox="0 0 472 12">
    <line x1="0" y1="6" x2="210" y2="6" stroke="#555" stroke-width="1.5"/>
    <circle cx="224" cy="6" r="3" fill="#444"/><circle cx="236" cy="6" r="3" fill="#444"/><circle cx="248" cy="6" r="3" fill="#444"/>
    <line x1="262" y1="6" x2="472" y2="6" stroke="#555" stroke-width="1.5"/>
  </svg>
  <div class="abs who-text">
    <p>Software is a leading provider of data warehouse and business intelligence solutions. We help our customers create vision and define a technology strategy aligned to maximize operational efficiencies. We are an adept group of analysts, designers, programmers, and general business and technology enthusiasts that share a common goal of helping our customers succeed. Our diverse expertise allows us to approach business challenges from a unique perspective, as we never let technology limitations restrict our ability to solve a problem.</p>
    <p>Our diverse expertise allows us to approach business challenges from a unique perspective, as we never let technology limitations restrict our ability to solve a problem.</p>
  </div>
</section>

<section class="abs services">
  <h2 class="abs section-title">Our Services</h2>
  <div class="abs title-rule"></div>

  <article class="abs service-card is-active" style="left:48px">
    <div class="service-icon"><svg viewBox="0 0 24 24"><path d="M12 3c3 5 6 8 6 12a6 6 0 0 1-12 0c0-4 3-7 6-12z" fill="#fff"/></svg></div>
    <h3 class="service-name">System Selection</h3>
    <p class="service-desc">dolore magna aliqua. Ut enim ad minim veniam, quis nostrud exercitation ullamco laboris nisi ut adolore magna aliqua magna aliq.</p>
    <div class="btn-order">Order Now...</div>
  </article>

  <article class="abs service-card" style="left:272px">
    <div class="service-icon"><svg viewBox="0 0 24 24"><path d="M4 19c2-8 8-13 16-14-1 8-6 13-14 13z" fill="#f15a22"/><path d="M4 20l9-9" stroke="#fff" stroke-width="1.5"/></svg></div>
    <h3 class="service-name">Accounting Systems &amp;<br>Conversions</h3>
    <p class="service-desc">dolore magna aliqua. Ut enim ad minim veniam, quis nostrud exercitation ullamco laboris nisi ut adolore magna aliqua magna aliq.</p>
    <div class="btn-order">Order Now...</div>
  </article>

  <article class="abs service-card" style="left:493px">
    <div class="service-icon"><svg viewBox="0 0 24 24"><rect x="3" y="4" width="18" height="12" rx="1" fill="#f15a22"/><rect x="10" y="16" width="4" height="3" fill="#f15a22"/><rect x="7" y="19" width="10" height="2" fill="#f15a22"/></svg></div>
    <h3 class="service-name">Integration</h3>
    <p class="service-desc">dolore magna aliqua. Ut enim ad minim veniam, quis nostrud exercitation ullamco laboris nisi ut adolore magna aliqua magna aliq.</p>
    <div class="btn-order">Order Now...</div>
  </article>

  <article class="abs service-card" style="left:714px">
    <div class="service-icon"><svg viewBox="0 0 24 24" fill="none" stroke="#f15a22" stroke-width="2"><path d="M12 3a6 6 0 0 0-3.5 10.9V17h7v-3.1A6 6 0 0 0 12 3z"/><path d="M9.5 20h5"/></svg></div>
    <h3 class="service-name">Business Inventory</h3>
    <p class="service-desc">dolore magna aliqua. Ut enim ad minim veniam, quis nostrud exercitation ullamco laboris nisi ut adolore magna aliqua magna aliq.</p>
    <div class="btn-order">Order Now...</div>
  </article>

  <article class="abs service-card" style="left:936px">
    <div class="service-icon"><svg viewBox="0 0 24 24" fill="none" stroke="#f15a22" stroke-width="2.2"><rect x="4" y="4" width="16" height="16" rx="2"/><path d="M8 12l3 3 6-7"/></svg></div>
    <h3 class="service-name">Business Project &amp; Job<br>Management</h3>
    <p class="service-desc">dolore magna aliqua. Ut enim ad minim veniam, quis nostrud exercitation ullamco laboris nisi ut adolore magna aliqua magna aliq.</p>
    <div class="btn-order">Order Now...</div>
  </article>
</section>

<section class="abs experts">
  <div class="abs experts-photo" role="img" aria-label="Darkened photo of a businessman in a suit holding a tablet"></div>
  <h2 class="abs experts-title">Ask Our Experts</h2>
  <blockquote class="abs quote">"Varden Software's reputation for extensive knowledge of business intelligence analytics has a well-founded basis. Partnering with them was a win-win from day one onward, repeatedly demonstrated by our teams working together in unified fashion to quickly identify and resolve technical issues while delivering highly valued solutions that solved difficult market problems. A solid talented group of professionals who are a pleasure to engage with."</blockquote>
  <div class="abs quote-author">Dr. Alan Restrepo, Vice President/General Manager - Analytics, Leading Healthcare IT Company</div>
  <div class="abs slider-dots"><span></span><span></span><span></span></div>
  <div class="abs btn-outline">READ MORE</div>
</section>

<footer class="abs site-footer">
  <h4 class="abs footer-heading" style="left:64px">STORE LOCATIONS</h4>
  <div class="abs map" role="img" aria-label="Street map showing the store location"></div>
  <ul class="abs footer-list" style="left:64px;top:196px">
    <li>48 Lorem Avenue, California, USA.</li>
    <li>(+84) 0198 765 432</li>
    <li>hello@example.com</li>
  </ul>

  <h4 class="abs footer-heading" style="left:411px">ACCOUNT</h4>
  <ul class="abs footer-list" style="left:411px;top:72px">
    <li>Your account</li><li>Checkout</li><li>Login</li><li>Register</li>
  </ul>

  <h4 class="abs footer-heading" style="left:626px">INFOMARTIONS</h4>
  <ul class="abs footer-list" style="left:626px;top:78px">
    <li>About Us</li><li>Contact Us</li><li>Terms &amp; Conditions</li><li>Faq</li>
  </ul>

  <h4 class="abs footer-heading" style="left:934px">GET SOCIAL</h4>
  <div class="abs social">
    <span style="background:#3b5a99"></span><span style="background:#1da1f2"></span><span style="background:#4a7aa8"></span><span style="background:#c8232c"></span><span style="background:#1abc9c"></span>
    <span style="background:#c4302b"></span><span style="background:#dd6b5a"></span>
  </div>
  <div class="abs btn-subscribe">SUBSCRIBE</div>
</footer>

<div class="abs copyright-bar">© Copyright 2016 HARBOURLY.COM.</div>
<div class="abs cards"><span>PAYLO</span><span>CARDEX</span><span>AMTRIX</span></div>

</body>
</html>
```